Upgrade Existing Web Design for an Investments Firm

We need a web designer for a company based in Dubai called Harborline Capital. We have an existing website which needs certain additions and changes. The design should be similar to typical corporate finance company websites. We're providing you with the link of our current website below - http://harborlinegroup.ae/
We would require the mock-ups to be ready in c. 7 working days and another 7 working days for the coding implementation. Timeline and promp response is very important for us as a client.

Target Market(s)

Investors/Consumer Brands/Financial Service Institutions/ Job Seekers

Industry/Entity Type

Financial Service

Coding

Coded - Design and coding required

Number of Pages Required

5+ page

Font styles to use
Other font styles liked:
• Arial

Colors
f04a51
000000
919191
cbcbcb

Requirements
Nice to have
• It should be similar to https://www.tovrenholdings.com
• Mobile Optimised as well

```html
<!DOCTYPE html>
<html lang="en">
<head>
<meta charset="utf-8">
<title>Harborline Partners &amp; Co</title>
<link href="https://fonts.googleapis.com/css2?family=Lato:wght@400;700;900&display=swap" rel="stylesheet">
<style>
:root{
  --red:#f0141e;
  --ink:#1a1a1a;
  --text:#555;
  --grey:#919191;
  --grey-light:#cbcbcb;
  --disc:#a5a5a5;
  --band:#ededed;
  --white:#fff;
  --social:#3b5bab;
  --client:#2f6f3e;
}
*{margin:0;padding:0;box-sizing:border-box}
html,body{width:1200px;height:3364px;overflow:hidden}
body{font-family:"Lato",Arial,sans-serif;color:var(--ink);background:var(--white);position:relative}
.abs{position:absolute}
/* header */
.brand{left:130px;top:28px;display:flex;align-items:center;gap:10px}
.brand-mark{width:34px;height:34px;background:var(--red)}
.brand-name{font-size:26px;font-weight:700;color:#555;letter-spacing:1px;line-height:1}
.brand-sub{font-size:9px;letter-spacing:3px;color:var(--red);margin-top:3px}
.follow-top{right:130px;top:22px;display:flex;align-items:center;gap:8px;font-size:12px}
.social{width:22px;height:22px;background:var(--social);display:inline-block}
.search{width:24px;height:24px;border:1px solid var(--grey-light);margin-left:20px}
.nav{right:128px;top:64px;display:flex;gap:36px;font-size:13px;align-items:center}
.nav a{color:var(--ink);text-decoration:none}
.nav .active{background:var(--red);color:#fff;padding:4px 9px}
/* hero */
.hero{left:0;top:105px;width:1200px;height:600px}
.hero-title{left:218px;top:162px;width:600px;font-size:30px;font-weight:700;line-height:38px;color:#fff}
.btn-red{background:var(--red);color:#fff;font-size:14px;font-weight:700;padding:10px 26px;display:inline-block}
.hero-btn{left:224px;top:305px}
.arrow-btn{width:42px;height:42px;border-radius:50%;background:rgba(0,0,0,.6);top:377px}
.arrow-btn svg{width:42px;height:42px;display:block}
/* section titles */
.title{left:0;width:1200px;text-align:center}
.title .small{font-size:22px;font-weight:700;letter-spacing:.5px}
.title .big{font-size:27px;font-weight:700;color:var(--red);margin-top:6px}
/* pillars */
.pillar{width:90px;text-align:center}
.pillar .bar{width:26px;margin:0 auto;background:var(--grey-light)}
.pillar .dot{width:84px;height:84px;border-radius:50%;background:var(--disc);margin:0 auto -4px;border:4px solid #fff;position:relative;z-index:1}
.pillar .dot svg{width:76px;height:76px;display:block}
.pillar.on .dot{background:var(--red)}
.pillar.on .bar{background:var(--red)}
.pillar .lbl{font-size:14px;color:var(--text);margin-top:18px;line-height:19px;margin-left:-20px;margin-right:-20px}
.pillar.on .lbl{color:var(--red)}
.info{left:157px;top:1295px;width:875px;height:185px;background:var(--band);padding:30px 60px 0 80px;font-size:14px;line-height:22px;color:var(--text)}
.info li{list-style:none;position:relative;margin-bottom:38px}
.info li::before{content:"";position:absolute;left:-36px;top:7px;width:8px;height:8px;border-radius:50%;background:var(--red)}
/* news */
.band{left:0;width:1200px;background:var(--band)}
.card{width:442px;height:176px;background:#fff;border:1px solid #ddd;top:1704px;display:flex;padding:24px 22px}
.card .photo{width:110px;height:117px;flex:none}
.card .body{margin-left:30px}
.card h3{font-size:15px;font-weight:700;margin:6px 0 14px}
.card p{font-size:11px;line-height:17px;color:#666}
.card .more{font-size:10px;color:var(--red);margin-top:14px}
.chev{top:1762px;font-size:40px;color:#999;line-height:1}
/* strategic */
.stairs{left:265px;top:2108px;width:660px;height:262px}
.stage-lbl{font-size:14px;color:var(--text)}
.btn-outline{left:538px;top:2452px;width:124px;height:42px;border:1px solid var(--red);color:var(--red);font-size:14px;text-align:center;line-height:40px}
/* clients */
.client{top:2730px;width:175px;height:74px;background:#fff;border:1px solid #ddd;display:flex;align-items:center;justify-content:center;gap:8px;font-size:15px;font-weight:700;color:var(--client)}
.client .sq{width:14px;height:14px;background:var(--client)}
.tip{left:500px;top:2825px;width:202px;height:64px;background:#fff;border:1px solid #ddd;font-size:11px;text-align:center;line-height:18px;padding-top:13px;color:#444}
/* footer */
.fcol h4{font-size:11px;color:var(--red);font-weight:400;margin-bottom:20px;letter-spacing:.5px}
.fcol{font-size:11px;color:#444;line-height:22px}
.crow{display:flex;gap:16px;margin-bottom:20px;line-height:18px}
.crow svg{width:12px;height:12px;flex:none;margin-top:3px}
.field{width:236px;height:50px;border:1px solid #ccc;padding:14px 0 0 22px;font-size:11px;color:#666;margin-bottom:18px}
.signup{margin-left:136px;padding:10px 18px;font-size:13px}
.rule{left:130px;top:3240px;width:940px;height:1px;background:#ddd}
.bottom{top:3283px;font-size:11px}
</style>
</head>
<body>

<header>
  <div class="abs brand">
    <span class="brand-mark"></span>
    <div><div class="brand-name">HARBORLINE</div><div class="brand-sub">PARTNERS &amp; CO</div></div>
  </div>
  <div class="abs follow-top">Follow us <span class="social" aria-label="social link"></span><span class="social" aria-label="social link"></span><span class="search"></span></div>
  <nav class="abs nav">
    <a class="active">Home</a><a>About Us</a><a>Approach</a><a>Portfolio</a><a>People</a><a>Contact Us</a>
  </nav>
</header>

<section>
  <svg class="abs hero" viewBox="0 0 1200 600" role="img" aria-label="Night skyline of a city marina with tall towers and lit streets">
    <defs>
      <linearGradient id="sky" x1="0" y1="0" x2="0" y2="1">
        <stop offset="0" stop-color="#54627a"/><stop offset=".45" stop-color="#3a3f55"/>
        <stop offset=".75" stop-color="#7a5638"/><stop offset="1" stop-color="#2a2f3e"/>
      </linearGradient>
    </defs>
    <path d="M0 0H1200V555Q900 525 600 585Q300 540 0 580Z" fill="url(#sky)"/>
    <path d="M0 580Q300 540 600 585Q900 525 1200 555" fill="none" stroke="#dcdcdc" stroke-width="5"/>
  </svg>
  <h1 class="abs hero-title">Harborline Partners &amp; Co is the #1<br>specialist retail and consumer<br>products investment firm in GCC</h1>
  <span class="abs btn-red hero-btn">READ MORE</span>
  <span class="abs arrow-btn" style="left:62px"><svg viewBox="0 0 42 42"><path d="M24 14l-7 7 7 7" stroke="#fff" stroke-width="3" fill="none"/></svg></span>
  <span class="abs arrow-btn" style="left:1110px"><svg viewBox="0 0 42 42"><path d="M18 14l7 7-7 7" stroke="#fff" stroke-width="3" fill="none"/></svg></span>
  <svg class="abs" style="left:573px;top:660px" width="54" height="54" viewBox="0 0 54 54"><circle cx="27" cy="27" r="26" fill="#fff" stroke="#ddd"/><path d="M20 22l7 6 7-6M20 29l7 6 7-6" stroke="#888" stroke-width="2" fill="none"/></svg>
</section>

<section>
  <div class="abs title" style="top:745px"><div class="small">WHY</div><div class="big">Harborline Capital?</div></div>

  <div class="abs pillar" style="left:155px;top:995px"><div class="dot"><svg viewBox="0 0 76 76"><circle cx="38" cy="34" r="12" fill="none" stroke="#fff" stroke-width="3"/><text x="38" y="39" text-anchor="middle" font-family="Lato,Arial,sans-serif" font-size="14" font-weight="700" fill="#fff">$</text><path d="M22 52h32" stroke="#fff" stroke-width="3"/></svg></div><div class="bar" style="height:140px"></div><div class="lbl">Specialist<br>Investor</div></div>
  <div class="abs pillar" style="left:285px;top:940px"><div class="dot"><svg viewBox="0 0 76 76"><path d="M26 50h26M30 48V38M36 48V32M42 48V36M48 48V28" stroke="#fff" stroke-width="3"/></svg></div><div class="bar" style="height:195px"></div><div class="lbl">Operational &amp;<br>Business Risk</div></div>
  <div class="abs pillar" style="left:420px;top:890px"><div class="dot"><svg viewBox="0 0 76 76"><circle cx="38" cy="30" r="10" fill="none" stroke="#fff" stroke-width="3"/><text x="38" y="35" text-anchor="middle" font-family="Lato,Arial,sans-serif" font-size="12" font-weight="700" fill="#fff">$</text><path d="M22 48q16 8 32 0" fill="none" stroke="#fff" stroke-width="3"/></svg></div><div class="bar" style="height:245px"></div><div class="lbl">Investment<br>Positioning</div></div>
  <div class="abs pillar on" style="left:552px;top:850px"><div class="dot"><svg viewBox="0 0 76 76"><rect x="24" y="28" width="28" height="20" rx="2" fill="none" stroke="#fff" stroke-width="3"/><path d="M30 35h6M30 41h16" stroke="#fff" stroke-width="3"/></svg></div><div class="bar" style="height:285px"></div><div class="lbl">Investment<br>Credentials</div></div>
  <div class="abs pillar" style="left:690px;top:890px"><div class="dot"><svg viewBox="0 0 76 76"><g fill="#fff"><circle cx="28" cy="32" r="4"/><circle cx="38" cy="30" r="5"/><circle cx="48" cy="32" r="4"/><rect x="22" y="38" width="12" height="10" rx="3"/><rect x="31" y="37" width="14" height="13" rx="3"/><rect x="42" y="38" width="12" height="10" rx="3"/></g></svg></div><div class="bar" style="height:245px"></div><div class="lbl">Investment<br>Team</div></div>
  <div class="abs pillar" style="left:825px;top:940px"><div class="dot"><svg viewBox="0 0 76 76"><rect x="33" y="24" width="10" height="8" fill="#fff"/><rect x="22" y="44" width="10" height="8" fill="#fff"/><rect x="44" y="44" width="10" height="8" fill="#fff"/><path d="M38 32v6M27 44v-6h22v6" stroke="#fff" stroke-width="2" fill="none"/></svg></div><div class="bar" style="height:195px"></div><div class="lbl">Management<br>Team</div></div>
  <div class="abs pillar" style="left:955px;top:995px"><div class="dot"><svg viewBox="0 0 76 76"><path d="M50 38a12 12 0 1 1-4-9" fill="none" stroke="#fff" stroke-width="3"/><path d="M47 22l0 8-8 0" fill="none" stroke="#fff" stroke-width="3"/><text x="38" y="43" text-anchor="middle" font-family="Lato,Arial,sans-serif" font-size="13" font-weight="700" fill="#fff">$</text></svg></div><div class="bar" style="height:140px"></div><div class="lbl">Investment<br>Pipeline</div></div>

  <ul class="abs info">
    <li>The founder of Harborline Capital, Lorena Vasquez brings extensive experience in venture capital and private equity in GCC across fundraising, investment and exit</li>
    <li>Harborline Capital partnered with STRIDEL Footwear in July 2016 and introduced the sneaker concept in GCC and other emerging markets</li>
  </ul>
</section>

<section>
  <div class="abs band" style="top:1540px;height:392px"></div>
  <div class="abs title" style="top:1585px"><div class="small">LATEST</div><div class="big">NEWS &amp; EVENTS</div></div>
  <span class="abs chev" style="left:66px">&#8249;</span>
  <span class="abs chev" style="left:1100px">&#8250;</span>
  <article class="abs card" style="left:130px">
    <div class="photo" role="img" aria-label="Photo of shoppers' legs and shopping bags" style="background:linear-gradient(135deg,#b98a7a,#6e7f98)"></div>
    <div class="body"><h3>Key insights for retail sector in GCC</h3><p>Retail and consumer products in GCC is estimated at USD 59 bn and expected to growth at a CAGR of 6% by 2020.</p><div class="more">READ MORE &#9656;</div></div>
  </article>
  <article class="abs card" style="left:626px">
    <div class="photo" role="img" aria-label="Photo of a hand holding a shopping bag" style="background:linear-gradient(135deg,#c98a8a,#a33a4a)"></div>
    <div class="body"><h3>Omni-channel as market entry strategy</h3><p>GCC is ranked in the top 10 global growth omnichannel markets due to degree of digitization, consumer behavior...</p><div class="more">READ MORE &#9656;</div></div>
  </article>
</section>

<section>
  <div class="abs title" style="top:1990px"><div class="small">STRATEGIC</div><div class="big">INVESTMENT</div></div>
  <div class="abs stairs" role="img" aria-label="Illustration of a four-stage staircase of business growth from idea to reinvention" style="background:linear-gradient(160deg,#f7f7f7,#ececec)"></div>
  <span class="abs stage-lbl" style="left:271px;top:2383px">Design and innovation</span>
  <span class="abs stage-lbl" style="left:431px;top:2343px">Roll-out growth</span>
  <span class="abs stage-lbl" style="left:592px;top:2314px">Maturity</span>
  <span class="abs stage-lbl" style="left:751px;top:2285px">Reinvention</span>
  <span class="abs btn-outline">Read More</span>
</section>

<section>
  <div class="abs band" style="top:2570px;height:376px"></div>
  <div class="abs title" style="top:2615px"><div class="small">OUR</div><div class="big">CLIENTS</div></div>
  <div class="abs client" style="left:130px"><span class="sq"></span>Dunecrest</div>
  <div class="abs client" style="left:320px"><span class="sq"></span>Saffra Foods</div>
  <div class="abs client" style="left:512px"><span class="sq"></span>Oasira</div>
  <div class="abs client" style="left:703px"><span class="sq"></span>Meridune</div>
  <div class="abs client" style="left:893px"><span class="sq"></span>Palmreach</div>
  <div class="abs tip">Buy Side M&amp;A for USD 50 million<br>Sector: FMCG &nbsp;|&nbsp; July 2016</div>
</section>

<footer>
  <div class="abs brand" style="top:3010px">
    <span class="brand-mark"></span>
    <div><div class="brand-name">HARBORLINE</div><div class="brand-sub">PARTNERS &amp; CO</div></div>
  </div>
  <div class="abs fcol" style="left:383px;top:2995px;width:260px">
    <h4>CONTACT US</h4>
    <div class="crow"><svg viewBox="0 0 12 12"><path d="M6 11L2 5a4 4 0 118 0z" fill="#888"/></svg><span>Office 1807, Crescent Point Office Tower<br>Dubai, United Arab Emirates</span></div>
    <div class="crow"><svg viewBox="0 0 12 12"><path d="M2 1h3l1 3-2 1a7 7 0 003 3l1-2 3 1v3C5 11 1 7 2 1z" fill="#888"/></svg><span>0097140000000</span></div>
    <div class="crow"><svg viewBox="0 0 12 12"><rect x="1" y="2" width="10" height="8" fill="none" stroke="#888"/><path d="M1 2l5 4 5-4" fill="none" stroke="#888"/></svg><span>info@harborlinegroup.ae</span></div>
  </div>
  <div class="abs fcol" style="left:693px;top:2995px">
    <h4>MENU</h4>
    Home<br>About Us<br>Our Approach<br>Our Portfolio<br>Our People<br>Contact
  </div>
  <div class="abs fcol" style="left:830px;top:2995px">
    <h4>NEWSLETTER SIGNUP!</h4>
    <div class="field">&#9993;&nbsp;&nbsp; E-mail id</div>
    <span class="btn-red signup">SIGNUP!</span>
  </div>
  <div class="abs rule"></div>
  <div class="abs bottom" style="left:130px;display:flex;align-items:center;gap:10px;color:var(--red)">FOLLOW US : <span class="social"></span><span class="social"></span></div>
  <div class="abs bottom" style="right:130px;top:3288px">Copyrights @ 2017 All Rights Reserved</div>
</footer>

</body>
</html>
```